Custom Truck shop New Business Card design

double sided business card including my new logo, brand colors and picking a font I attached, clean and modern look. I attached the old card for some reference. and would like to include the picture of the white truck attached. I would also like to have it with one of my employees info as well. (same info except name and title Brin Tolvay Service Writer)

Dale Porvick
Owner

address
48310 E Calloway Ridge Rd S
STE 217
Marsh Hollow, CO 80219

phone 720-555-0184

email dale@brokenspurrigs.example

website brokenspurrgis.example

social @brokenspurrigs

Target Market(s)

men 18-60

Industry/Entity Type

Automotive

Contact Information for Business Card

Dale Porvick Owner address 48310 E Calloway Ridge Rd S STE 217 Marsh Hollow, CO 80219 phone 720-555-0184 email dale@brokenspurrigs.example website brokenspurrgis.example social @brokenspurrigs

Font styles to use
Other font styles liked:
• fonts attached

Requirements
Must have
• new logo, orange #FC68D, Charcoal #333333
Nice to have
• the white truck

```html
<!DOCTYPE html>
<html lang="en">
<head>
<meta charset="utf-8">
<title>Broken Spur Rigs – Business Card</title>
<link rel="stylesheet" href="https://fonts.googleapis.com/css2?family=Montserrat:wght@400;500;600;700;800&display=swap">
<style>
  :root {
    --orange: #f26a2e;
    --charcoal: #333333;
    --charcoal-deep: #2b2b2b;
    --ink: #1f1f1f;
    --paper: #ffffff;
    --backdrop: #c4c4c4;
  }
  * { margin: 0; padding: 0; box-sizing: border-box; }
  html, body {
    width: 1200px; height: 815px; overflow: hidden;
    background: var(--backdrop);
    font-family: "Montserrat", Arial, sans-serif;
  }
  .sheet { position: relative; width: 1200px; height: 815px; }
  .card {
    position: absolute; top: 253px;
    width: 540px; height: 309px;
    border-radius: 22px; overflow: hidden;
  }
  .card--front { left: 40px; background: var(--paper); color: var(--ink); }
  .card--back { left: 620px; background: var(--charcoal); }

  /* front: brand lockup */
  .brand { position: absolute; right: 26px; top: 32px; display: flex; align-items: center; gap: 12px; }
  .brand__mark { width: 56px; height: 56px; border-radius: 50%; background: var(--charcoal); flex: none; }
  .brand__name { font-weight: 800; font-size: 20px; letter-spacing: 0.4px; color: var(--charcoal); text-transform: uppercase; white-space: nowrap; }
  .brand-rule { position: absolute; right: 26px; top: 98px; width: 230px; height: 1.5px; background: var(--orange); }

  /* front: person */
  .person-tab { position: absolute; left: 0; top: 168px; width: 16px; height: 36px; background: var(--orange); }
  .person__name { position: absolute; left: 30px; top: 164px; font-size: 25px; font-weight: 700; color: var(--orange); text-transform: uppercase; letter-spacing: 0.3px; white-space: nowrap; }
  .person__title { position: absolute; left: 30px; top: 196px; font-size: 13px; font-weight: 500; color: var(--ink); text-transform: uppercase; }
  .divider { position: absolute; left: 30px; top: 222px; width: 490px; height: 1.5px; background: var(--orange); }

  .contacts { position: absolute; left: 30px; top: 234px; list-style: none; }
  .contacts li { display: flex; align-items: center; gap: 8px; font-size: 12.5px; line-height: 20px; color: var(--ink); white-space: nowrap; }
  .contacts svg { width: 11px; height: 11px; flex: none; fill: var(--orange); }

  .address { position: absolute; right: 24px; top: 234px; text-align: right; font-size: 12.5px; line-height: 18px; font-style: normal; color: var(--ink); white-space: nowrap; }

  /* back */
  .back-mark {
    position: absolute; left: 225px; top: 58px; width: 90px; height: 90px; border-radius: 50%;
    background: var(--charcoal-deep);
    box-shadow: inset 2px 2px 3px rgba(0,0,0,0.45), 0 1px 0 rgba(255,255,255,0.08);
  }
  .back-name {
    position: absolute; left: 0; right: 0; top: 168px; text-align: center;
    font-weight: 800; font-size: 30px; letter-spacing: 0.5px; text-transform: uppercase;
    color: var(--charcoal-deep); text-shadow: 0 1px 0 rgba(255,255,255,0.07); white-space: nowrap;
  }
  .back-rule { position: absolute; left: 90px; top: 214px; width: 360px; height: 1.5px; background: var(--charcoal-deep); }
  .follow {
    position: absolute; left: 0; right: 0; top: 238px; text-align: center;
    font-size: 14px; font-weight: 500; color: var(--paper); white-space: nowrap;
  }
  .follow__label { color: var(--orange); font-weight: 600; text-transform: uppercase; letter-spacing: 0.5px; }
</style>
</head>
<body>
<main class="sheet">
  <section class="card card--front" aria-label="Business card front">
    <div class="brand">
      <span class="brand__mark" aria-hidden="true"></span>
      <span class="brand__name">Broken Spur Rigs</span>
    </div>
    <div class="brand-rule"></div>

    <div class="person-tab"></div>
    <h1 class="person__name">Dale Porvick</h1>
    <p class="person__title">Owner</p>
    <div class="divider"></div>

    <ul class="contacts">
      <li>
        <svg viewBox="0 0 24 24" aria-hidden="true"><path d="M6.6 10.8a15.1 15.1 0 0 0 6.6 6.6l2.2-2.2a1 1 0 0 1 1-.25 11.4 11.4 0 0 0 3.6.57 1 1 0 0 1 1 1V20a1 1 0 0 1-1 1A17 17 0 0 1 3 4a1 1 0 0 1 1-1h3.5a1 1 0 0 1 1 1c0 1.25.2 2.45.57 3.57a1 1 0 0 1-.25 1z"/></svg>
        720-555-0184
      </li>
      <li>
        <svg viewBox="0 0 24 24" aria-hidden="true"><path d="M2 5h20v14H2z"/><path d="M2 6.5l10 8 10-8V5H2z" fill="#fff" opacity="0.9"/></svg>
        dale@brokenspurrigs.example
      </li>
      <li>
        <svg viewBox="0 0 24 24" aria-hidden="true"><path d="M12 2a10 10 0 1 0 0 20 10 10 0 0 0 0-20zm6.9 6h-2.9a15.7 15.7 0 0 0-1.4-3.6A8 8 0 0 1 18.9 8zM12 4c.8 1.2 1.5 2.5 1.9 4h-3.8c.4-1.5 1.1-2.8 1.9-4zM4.3 14a8.2 8.2 0 0 1 0-4h3.4a16.5 16.5 0 0 0 0 4zm.8 2h2.9c.3 1.3.8 2.5 1.4 3.6A8 8 0 0 1 5.1 16zM8 8H5.1a8 8 0 0 1 4.3-3.6C8.8 5.5 8.3 6.7 8 8zm4 12c-.8-1.2-1.5-2.5-1.9-4h3.8c-.4 1.5-1.1 2.8-1.9 4zm2.3-6H9.7a14.7 14.7 0 0 1 0-4h4.6a14.7 14.7 0 0 1 0 4zm.3 5.6c.6-1.1 1.1-2.3 1.4-3.6h2.9a8 8 0 0 1-4.3 3.6zM16.3 14a16.5 16.5 0 0 0 0-4h3.4a8.2 8.2 0 0 1 0 4z"/></svg>
        www.brokenspurrgis.example
      </li>
    </ul>

    <address class="address">
      48310 E Calloway Ridge Rd S<br>
      STE 217<br>
      Marsh Hollow, CO 80219
    </address>
  </section>

  <section class="card card--back" aria-label="Business card back">
    <div class="back-mark" aria-hidden="true"></div>
    <p class="back-name">Broken Spur Rigs</p>
    <div class="back-rule"></div>
    <p class="follow"><span class="follow__label">Follow us :-</span> @brokenspurrigs</p>
  </section>
</main>
</body>
</html>
```